Business Card Design Project

We need a Business Card for an Mechanical Engineering firm in Singapore. The design should be Modern & Technical looking, yet eye catching.

Our company deals in Cutting Tools & Machine Accessories for the Manufacturing Industries such as Oil & Gas, Aero Space, etc... For more information on our Company, you can either email me or view our website www.valtrion.com.sg.

We are trying to revamp our image to give our consumers a fresh new perspective to our company, so we welcome all ideas.

Industry/Entity Type

Business

Requirements
Must have
• Must incorporate New Company Logo into the card as shown in Uploaded file.

```html
<!DOCTYPE html>
<html lang="en">
<head>
<meta charset="utf-8">
<title>Valtrion Tools – Business Card</title>
<link href="https://fonts.googleapis.com/css2?family=Exo+2:wght@400&display=swap" rel="stylesheet">
<style>
  :root {
    --page: #ffffff;
    --page-edge: #c8c8c8;
    --card-yellow: #edcf00;
    --motif-tone: rgba(230, 180, 0, 0.55);
    --line-bright: #f6f200;
    --line-amber: #e3b000;
    --ink: #1a1400;
    --brand-maroon: #7d0a2e;
  }
  html, body {
    margin: 0;
    padding: 0;
    overflow: hidden;
  }
  body {
    width: 1200px;
    height: 838px;
    background: var(--page);
    font-family: "Exo 2", sans-serif;
  }
  .canvas {
    position: relative;
    width: 1200px;
    height: 838px;
    box-sizing: border-box;
    border: 1px solid var(--page-edge);
    overflow: hidden;
  }
  .business-card {
    position: absolute;
    left: 277px;
    top: 243px;
    width: 594px;
    height: 303px;
    background: var(--card-yellow);
    overflow: hidden;
    box-shadow: -1px 1px 0 #b9a200;
  }
  .motif-area {
    position: absolute;
    left: 150px;
    top: -60px;
    width: 450px;
    height: 360px;
    background: radial-gradient(ellipse at 50% 50%, var(--motif-tone) 0%, rgba(230, 180, 0, 0.25) 45%, transparent 72%);
  }
  .accent-lines {
    position: absolute;
    inset: 0;
  }
  .brand {
    position: absolute;
    left: 33px;
    top: 226px;
    display: flex;
    align-items: center;
    gap: 6px;
    color: var(--brand-maroon);
    font-size: 17px;
    letter-spacing: 0.5px;
  }
  .brand-dot {
    width: 14px;
    height: 14px;
    border-radius: 50%;
    background: var(--brand-maroon);
  }
  .contact {
    position: absolute;
    left: 351px;
    top: 46px;
    color: var(--ink);
    font-size: 15px;
    line-height: 19px;
  }
  .contact p { margin: 0; }
  .contact-name {
    font-size: 19px;
    line-height: 22px;
  }
  .contact-role { margin-top: 6px !important; }
  .company-address { margin-top: 35px !important; }
  .contact-lines { margin-top: 14px !important; }
</style>
</head>
<body>
<div class="canvas">
  <div class="business-card">
    <div class="motif-area" role="img" aria-label="Faint large gear decoration in the background"></div>

    <svg class="accent-lines" width="594" height="303" viewBox="0 0 594 303" aria-hidden="true">
      <line x1="110" y1="0" x2="196" y2="303" stroke="var(--line-amber)" stroke-width="2"/>
      <line x1="33" y1="0" x2="228" y2="303" stroke="var(--line-bright)" stroke-width="2"/>
    </svg>

    <div class="brand">
      <span class="brand-dot"></span>
      <span class="brand-name">VALTRION TOOLS</span>
    </div>

    <div class="contact">
      <p class="contact-name">Melissa</p>
      <p class="contact-role">Contact Person</p>
      <div class="company-address">
        <p>Valtrion Tools Pte Ltd</p>
        <p>58 Kallang Crest #03-12,</p>
        <p>Meridian Works Hub,</p>
        <p>Singapore 349214</p>
      </div>
      <div class="contact-lines">
        <p>Tel: 65-61234570</p>
        <p>Fax: 65-61234571</p>
        <p>mail: info@valtrion.com.sg</p>
      </div>
    </div>
  </div>
</div>
</body>
</html>
```